Tarnwickhub.com home page

On the existing home page I want to eliminate people in circles and promote these three earning opportunities:
1." Make a referral to existing advertiser"
Earn up to $5000 when you make a successful referral to one of our advertisers.
2."Sign up a new business to offer referral commisions to ambassaadors". Earn up to $5000 or more when you earn 5% of money paid out by business in referral fees.
3."Sign up new ambassadors"
Earn up to $5000 or more when you earn 5% of the money the ambassadors you sign up earn.

In each offer I want a learn more button .

Industry/Entity Type

Business

Font styles to use
Serif

```html
<!DOCTYPE html>
<html lang="en">
<head>
<meta charset="utf-8">
<title>TarnwickHub – Referral Marketplace</title>
<link rel="stylesheet" href="https://fonts.googleapis.com/css2?family=Roboto:wght@400;500;700&family=Open+Sans:wght@400;600&family=PT+Sans:wght@400;700&display=swap">
<style>
  :root {
    --green: #2aa95a;
    --green-dark: #1c7a22;
    --green-title: #2fa84f;
    --ink: #111111;
    --navy: #123a6b;
    --nav-text: #5b4a3c;
    --card-border: #c5cacd;
    --rule: #e4e6e8;
    --white: #ffffff;
    --hero-top: #edf2f6;
  }
  * { box-sizing: border-box; margin: 0; padding: 0; }
  html, body { width: 1200px; height: 668px; overflow: hidden; background: var(--white); }
  body { position: relative; font-family: "Open Sans", Arial, sans-serif; color: var(--ink); }

  .site-header { position: absolute; left: 0; top: 0; width: 1200px; height: 69px; background: var(--white); }
  .brand { position: absolute; left: 105px; top: 14px; font-family: "PT Sans", Arial, sans-serif; font-size: 34px; font-weight: 700; color: var(--green-title); letter-spacing: -0.5px; }
  .main-nav { position: absolute; top: 0; left: 739px; height: 69px; display: flex; }
  .main-nav a { display: flex; align-items: center; height: 69px; padding: 0 15px; font-size: 14px; color: var(--nav-text); text-decoration: none; font-family: "Open Sans", Arial, sans-serif; }
  .main-nav a.active { background: var(--green); color: var(--white); padding: 0 16px; margin-right: 0; }

  .hero-band { position: absolute; left: 0; top: 69px; width: 1200px; height: 56px; background: linear-gradient(var(--hero-top), var(--white)); }
  .hero-title { position: absolute; left: 0; width: 1200px; top: 86px; text-align: center; font-family: "Roboto", Arial, sans-serif; font-weight: 700; font-size: 37px; letter-spacing: 2px; color: var(--ink); }
  .hero-subtitle { position: absolute; left: 0; width: 1200px; top: 126px; text-align: center; font-family: "Roboto", Arial, sans-serif; font-weight: 500; font-size: 27px; color: var(--ink); }
  .hero-intro { position: absolute; left: 260px; top: 158px; width: 700px; font-size: 14.5px; line-height: 21px; color: var(--ink); }
  .hero-intro strong { color: #1c3d9a; font-weight: 600; }

  .offer { position: absolute; top: 226px; height: 281px; border: 4px solid var(--card-border); background: var(--white); text-align: center; }
  .offer-1 { left: 93px; width: 318px; }
  .offer-2 { left: 421px; width: 386px; }
  .offer-3 { left: 818px; width: 309px; }
  .offer-step { position: absolute; left: 50%; top: 16px; margin-left: -34px; width: 68px; height: 68px; border-radius: 50%; background: var(--green); border: 4px solid var(--white); box-shadow: 0 0 0 2px #c9cdd0; color: var(--white); font-family: "Roboto", Arial, sans-serif; font-weight: 700; font-size: 42px; line-height: 60px; }
  .offer-title { position: absolute; left: 0; right: 0; top: 100px; font-family: "PT Sans", Arial, sans-serif; font-weight: 700; font-size: 15.5px; line-height: 17px; color: var(--green-title); text-transform: uppercase; }
  .offer-text { position: absolute; left: 10px; right: 10px; top: 144px; font-size: 13px; line-height: 17px; color: var(--ink); }
  .offer-text .amount { font-size: 21px; }
  .offer-button { position: absolute; left: 50%; top: 202px; margin-left: -69px; width: 138px; height: 37px; background: var(--green); color: var(--white); font-size: 14px; display: flex; align-items: center; justify-content: center; gap: 10px; text-decoration: none; }

  .payout-rule { position: absolute; left: 0; top: 532px; width: 1200px; height: 1px; background: var(--rule); }
  .payout { position: absolute; left: 0; width: 1200px; top: 540px; text-align: center; font-family: "PT Sans", Arial, sans-serif; font-size: 31px; color: var(--navy); }
  .payout .total { font-size: 42px; font-weight: 700; color: var(--green-dark); margin-left: 8px; }

  .signup-band { position: absolute; left: 0; top: 597px; width: 1200px; height: 71px; background: var(--green); }
  .signup-text { position: absolute; left: 97px; top: 24px; font-size: 16px; font-weight: 600; color: var(--white); }
  .signup-button { position: absolute; left: 946px; top: 13px; width: 174px; height: 43px; border: 2px solid var(--white); color: var(--white); font-size: 16px; display: flex; align-items: center; justify-content: center; gap: 8px; text-decoration: none; }
</style>
</head>
<body>
  <header class="site-header">
    <div class="brand">TarnwickHub</div>
    <nav class="main-nav">
      <a class="active" href="#">Home</a>
      <a href="#">How It Works</a>
      <a href="#">Search</a>
      <a href="#">Members</a>
      <a href="#">Log In</a>
    </nav>
  </header>

  <div class="hero-band"></div>
  <h1 class="hero-title">EASILY MAKE MORE MONEY</h1>
  <h2 class="hero-subtitle">JUST BY REFERRING YOURSELF, YOUR FRIENDS OR BUSINESS ASSOCIATES</h2>
  <p class="hero-intro">These <strong>Top Ambassadors</strong> increased their annual income by 50% just by referring associates about services in our network!</p>

  <section class="offer offer-1">
    <div class="offer-step">1</div>
    <h3 class="offer-title">Make a referral to<br>existing advertiser</h3>
    <p class="offer-text">Earn up to <span class="amount">$5000</span> when you make a successful referral to one of our advertisers</p>
    <a class="offer-button" href="#">Learn More
      <svg width="9" height="14" viewBox="0 0 9 14"><path d="M2 1l6 6-6 6" fill="none" stroke="#fff" stroke-width="2.4"/></svg></a>
  </section>

  <section class="offer offer-2">
    <div class="offer-step">2</div>
    <h3 class="offer-title">Sign up a new business to offer<br>referral commisions to ambassaadors</h3>
    <p class="offer-text">Earn up to <span class="amount">$5000</span> or more when you earn 5%<br>of money paid out by business in referral fees</p>
    <a class="offer-button" href="#">Learn More
      <svg width="9" height="14" viewBox="0 0 9 14"><path d="M2 1l6 6-6 6" fill="none" stroke="#fff" stroke-width="2.4"/></svg></a>
  </section>

  <section class="offer offer-3">
    <div class="offer-step">3</div>
    <h3 class="offer-title">Sign up new<br>ambassadors</h3>
    <p class="offer-text">Earn up to <span class="amount">$5000</span> or more when you earn 5% of the money the ambassadors you sign up earn</p>
    <a class="offer-button" href="#">Learn More
      <svg width="9" height="14" viewBox="0 0 9 14"><path d="M2 1l6 6-6 6" fill="none" stroke="#fff" stroke-width="2.4"/></svg></a>
  </section>

  <div class="payout-rule"></div>
  <p class="payout">Tarnwick Hub has paid over <span class="total">$359,465 YTD</span></p>

  <footer class="signup-band">
    <p class="signup-text">TarnwickHub, Fastest Growing Referral Marketplace. Earn income just by referring people you know.</p>
    <a class="signup-button" href="#">
      <svg width="20" height="18" viewBox="0 0 20 18"><path d="M1 8h4v9H1zM5 9l4-7c1.5 0 2 1 1.7 2.5L10 7h7c1.2 0 2 1 1.7 2l-1.5 6c-.3 1-1 1.8-2 1.8H5" fill="none" stroke="#fff" stroke-width="1.5" stroke-linejoin="round"/></svg>
      Free to Sign Up!</a>
  </footer>
</body>
</html>
```